Pelkman Agency (http://pa.quorvexstudio.com/)

We are looking for a similar design to what we have, but more professional looking and cleaned up with links and logo that is not so grainy looking. We are an independent insurance agency marketing to personal and commercial clients. We offer all commercial lines markets and all personal lines. We target excavators, landscapers, restaurants, golf courses, contractors. Please look at http://pa.quorvexstudio.com/ which we had designed but do not like it, it will give you an idea of what we are looking for.

Target Market(s)

Commercial and personal insurance. All business products and all personal (homeowners, auto, antique auto, umbrella)

Industry/Entity Type

It Professional

Logo Text

Knowledge Building Your Assurance

Number of Pages Required

5+ page

Colors
000000
848484
0255a3

```html
<!DOCTYPE html>
<html lang="en">
<head>
<meta charset="utf-8">
<title>Pelkman Agency</title>
<link href="https://fonts.googleapis.com/css2?family=Open+Sans:wght@300;400;600;700&display=swap" rel="stylesheet">
<style>
:root{
  --ink:#000;
  --header:#141516;
  --footer:#121314;
  --footer-deep:#0c0d0e;
  --blue:#0255a3;
  --blue-dark:#063d8c;
  --blue-bright:#1463c8;
  --grey:#848484;
  --panel:#efefef;
  --text:#555;
  --white:#fff;
}
*{margin:0;padding:0;box-sizing:border-box}
html,body{width:862px;height:1200px;overflow:hidden;background:#fff}
body{position:relative;font-family:'Open Sans',Arial,sans-serif;color:var(--text)}
.abs{position:absolute}
.hero{left:0;top:0;width:862px;height:412px;background:radial-gradient(ellipse at 50% 45%,#5c6a78 0%,#3c4753 45%,#1e252d 100%)}
.header{left:0;top:0;width:862px;height:84px;background:rgba(18,19,20,.93)}
.brand{left:88px;top:30px;display:flex;align-items:center;gap:10px}
.brand-dot{width:30px;height:30px;border-radius:50%;background:#2a2c2e}
.brand-name{font-size:19px;font-weight:600;color:var(--white);letter-spacing:.2px}
.phone{left:690px;top:18px;font-size:10.5px;color:#ddd;display:flex;gap:8px;align-items:center}
.nav{top:45px;font-size:9.5px;color:#eee}
.nav.active{color:var(--blue-bright)}
.hero-title{left:0;width:862px;text-align:center;color:#fff}
.t1{top:188px;font-size:27px;font-weight:300}
.t2{top:219px;font-size:27px;font-weight:700}
.lead{top:262px;left:255px;width:352px;text-align:center;font-size:9.6px;color:#eee;line-height:16px}
.btn{background:var(--blue);color:#fff;font-size:8px;border-radius:3px;display:flex;align-items:center;justify-content:center}
.hero-btn{left:397px;top:313px;width:63px;height:27px}
.arrow{top:205px}
.band{left:0;top:412px;width:862px;height:122px;background:linear-gradient(180deg,var(--blue-bright),var(--blue-dark))}
.cell{top:412px;width:140px;height:122px;border-left:1px solid rgba(0,0,0,.18);display:flex;flex-direction:column;align-items:center;padding-top:28px;color:#fff;font-size:11.5px;font-weight:600}
.cell .ico{height:34px;display:flex;align-items:center;justify-content:center;margin-bottom:8px}
.feature{top:563px;width:180px;display:flex;flex-direction:column;align-items:center;text-align:center}
.feature .ring{width:60px;height:60px;border-radius:50%;background:#151515;display:flex;align-items:center;justify-content:center}
.feature h3{font-size:12px;font-weight:400;color:var(--blue);margin-top:11px}
.feature p{font-family:Arial,sans-serif;font-size:8.2px;line-height:14.5px;color:var(--grey);margin-top:6px;width:160px}
.feature .btn{width:43px;height:20px;margin-top:14px;border-radius:4px}
.sector-bg{left:0;top:766px;width:862px;height:178px;background:var(--panel)}
.sector{top:794px;width:226px}
.sector .pic{width:55px;height:55px;border-radius:50%}
.sector .k{left:65px;top:10px;font-size:12.5px;color:var(--blue);white-space:nowrap}
.sector .n{left:65px;top:24px;font-size:19px;color:#222;white-space:nowrap}
.sector p{position:absolute;top:70px;left:0;width:226px;font-family:Arial,sans-serif;font-size:7.6px;line-height:14.5px;color:var(--grey)}
.sector p b{display:block;font-weight:400;font-size:8.3px;color:#333;white-space:nowrap}
.rule{left:0;top:944px;width:862px;height:4px;background:var(--blue)}
.footer{left:0;top:948px;width:862px;height:204px;background:var(--footer)}
.footer h4{position:absolute;font-size:14px;font-weight:400;color:#fff}
.about{left:82px;top:1019px;width:231px;font-family:Arial,sans-serif;font-size:7.8px;line-height:13.2px;color:#eee;text-align:justify}
.row{font-family:Arial,sans-serif;font-size:8px;color:#eee;display:flex;gap:10px;align-items:flex-start;line-height:11px}
.row u{text-decoration:underline}
.bottom{left:0;top:1152px;width:862px;height:48px;background:var(--footer-deep)}
.copy{left:89px;top:1168px;font-family:Arial,sans-serif;font-size:8px;color:#eee}
.social{top:1167px;width:12px;height:12px;border-radius:50%;background:#cfcfcf}
</style>
</head>
<body>
<div class="abs hero" role="img" aria-label="Photo of businessmen in suits holding black umbrellas in the rain"></div>
<header class="abs header"></header>
<div class="abs brand"><span class="brand-dot"></span><span class="brand-name">Pelkman Agency</span></div>
<div class="abs phone"><svg width="10" height="10" viewBox="0 0 10 10"><path d="M2 1l2 2-1 1c.6 1.3 1.7 2.4 3 3l1-1 2 2-1.5 1.5C4 9 1 6 .5 2.5z" fill="#2f7bd8"/></svg>1-888-4 Pelkman</div>
<nav>
<span class="abs nav active" style="left:410px">HOME</span>
<span class="abs nav" style="left:469px">ABOUT US</span>
<span class="abs nav" style="left:546px">SERVICES</span>
<span class="abs nav" style="left:624px">SERVICE CENTER</span>
<span class="abs nav" style="left:727px">CONTACT US</span>
</nav>
<svg class="abs arrow" style="left:63px" width="20" height="38" viewBox="0 0 20 38"><path d="M18 1L2 19l16 18" stroke="#aab" stroke-width="1.5" fill="none"/></svg>
<svg class="abs arrow" style="left:780px" width="20" height="38" viewBox="0 0 20 38"><path d="M2 1l16 18L2 37" stroke="#aab" stroke-width="1.5" fill="none"/></svg>
<div class="abs hero-title t1">SMALL ENOUGH TO CARE</div>
<div class="abs hero-title t2">BIG ENOUGH TO MAKE A DIFFERENCE</div>
<p class="abs lead">Please find information about our agency, its principles , and the various types of insurance coverages that we provide.</p>
<div class="abs btn hero-btn">READ MORE</div>

<section class="abs band"></section>
<div class="abs cell" style="left:80px"><div class="ico"><svg width="32" height="24" viewBox="0 0 32 24"><rect x="1" y="3" width="30" height="18" rx="2" fill="none" stroke="#fff" stroke-width="2.5"/><circle cx="16" cy="12" r="5" fill="#fff"/></svg></div>Business Insurance</div>
<div class="abs cell" style="left:221px"><div class="ico"><svg width="34" height="24" viewBox="0 0 34 24"><path d="M7 4h20l4 9v8h-5v-3H8v3H3v-8z" fill="#fff"/><rect x="9" y="7" width="16" height="5" fill="#1556b4"/></svg></div>Auto Insurance</div>
<div class="abs cell" style="left:362px"><div class="ico"><svg width="34" height="28" viewBox="0 0 34 28"><circle cx="9" cy="6" r="4" fill="#fff"/><circle cx="25" cy="6" r="4" fill="#fff"/><circle cx="17" cy="10" r="5" fill="#fff"/><path d="M2 20c0-6 14-6 14 0zM18 20c0-6 14-6 14 0zM8 28c0-8 18-8 18 0z" fill="#fff"/></svg></div>Life Insurance</div>
<div class="abs cell" style="left:503px"><div class="ico"><svg width="30" height="26" viewBox="0 0 30 26"><path d="M15 2L2 13h4v11h7v-7h4v7h7V13h4z" fill="#fff"/></svg></div>Home Insurance</div>
<div class="abs cell" style="left:643px;border-right:1px solid rgba(0,0,0,.18)"><div class="ico"><svg width="30" height="26" viewBox="0 0 30 26"><rect x="2" y="6" width="26" height="18" rx="2" fill="#fff"/><rect x="10" y="1" width="10" height="6" rx="1" fill="none" stroke="#fff" stroke-width="2"/><rect x="2" y="13" width="26" height="2" fill="#1556b4"/></svg></div>Personal Insurance</div>

<div class="abs feature" style="left:76px"><div class="ring"><svg width="20" height="20" viewBox="0 0 20 20"><circle cx="10" cy="6" r="4.5" fill="#fff"/><path d="M2 19c0-8 16-8 16 0z" fill="#fff"/></svg></div><h3>FIND AN AGENT</h3><p>Lorem ipsum dolor sit amet, consectetuer adipiscing elit. Aenean commodo ligula eget dolor. Aenean massa.</p><div class="btn">MORE</div></div>
<div class="abs feature" style="left:251px"><div class="ring"><svg width="24" height="24" viewBox="0 0 24 24"><circle cx="12" cy="12" r="9" fill="none" stroke="#fff" stroke-width="4"/><circle cx="12" cy="12" r="4" fill="none" stroke="#fff" stroke-width="1.5"/></svg></div><h3>ANSWER CENTER</h3><p>Lorem ipsum dolor sit amet, consectetuer adipiscing elit. Aenean commodo ligula eget dolor. Aenean massa.</p><div class="btn">MORE</div></div>
<div class="abs feature" style="left:427px"><div class="ring"><svg width="28" height="22" viewBox="0 0 28 22"><ellipse cx="11" cy="9" rx="10" ry="8" fill="#fff"/><ellipse cx="19" cy="13" rx="8" ry="6.5" fill="#fff" stroke="#151515" stroke-width="1.5"/></svg></div><h3>GET A QUOTE</h3><p>Lorem ipsum dolor sit amet, consectetuer adipiscing elit. Aenean commodo ligula eget dolor. Aenean massa.</p><div class="btn">MORE</div></div>
<div class="abs feature" style="left:613px"><div class="ring"><svg width="22" height="22" viewBox="0 0 22 22"><rect x="2" y="9" width="5" height="11" fill="#fff"/><path d="M8 9l4-7c2 0 2 2 1.5 5H19c1.5 0 2 1.5 1.5 3l-2 8c-.3 1-1 2-2 2H8z" fill="#fff"/></svg></div><h3>CHALLENGE</h3><p>Lorem ipsum dolor sit amet, consectetuer adipiscing elit. Aenean commodo ligula eget dolor. Aenean massa.</p><div class="btn">MORE</div></div>

<section class="abs sector-bg"></section>
<div class="abs sector" style="left:82px"><div class="pic" role="img" aria-label="Photo of an excavator at work" style="background:linear-gradient(160deg,#6f9fd0,#c89a3a 70%,#8a6a3a)"></div><span class="abs k">INSURANCE FOR</span><span class="abs n">EXCAVATORS</span><p><b>Lorem ipsum dolor sit amet, consectetuer adipiscing elit.</b>Aenean commodo ligula eget dolor. Aenean massa. Cum sociis natoque penatibus et magnis dis parturient montes</p></div>
<div class="abs sector" style="left:321px"><div class="pic" role="img" aria-label="Photo of a landscaper mowing grass" style="background:linear-gradient(160deg,#3e7d30,#7dbb42 60%,#4d8a2a)"></div><span class="abs k">INSURANCE FOR</span><span class="abs n">LANDSCAPERS</span><p><b>Lorem ipsum dolor sit amet, consectetuer adipiscing elit.</b>Aenean commodo ligula eget dolor. Aenean massa. Cum sociis natoque penatibus et magnis dis parturient montes</p></div>
<div class="abs sector" style="left:558px"><div class="pic" role="img" aria-label="Photo of a restaurant table setting" style="background:linear-gradient(160deg,#5a3a22,#d8a050 55%,#7a4a24)"></div><span class="abs k">INSURANCE FOR</span><span class="abs n">RESTAURANTS</span><p><b>Lorem ipsum dolor sit amet, consectetuer adipiscing elit.</b>Aenean commodo ligula eget dolor. Aenean massa. Cum sociis natoque penatibus et magnis dis parturient montes</p></div>

<div class="abs rule"></div>
<footer class="abs footer">
<h4 style="left:82px;top:23px">ABOUT US</h4>
<h4 style="left:398px;top:26px">OUR LOCATIONS</h4>
<h4 style="left:601px;top:26px">CONTACT US</h4>
</footer>
<div class="abs about"><p>Established in 1950 by the Hollis family, the Pelkman Agency was founded on the philosophy of offering personal, professional service. Since then we have grown into a full service agency with a staff of 10 insurance specialist serving over 2,000 individuals and 800 businesses.</p><p style="margin-top:13px">We are an Independent Agency , which allows us to keep your needs in mind.</p></div>

<div class="abs row" style="left:398px;top:1019px"><span>☎</span>555-310-2000</div>
<div class="abs row" style="left:398px;top:1042px"><span>▤</span>555-310-7153</div>
<div class="abs row" style="left:398px;top:1065px"><span>✉</span><u>admin@pelkmanagency.com</u></div>
<div class="abs row" style="left:398px;top:1087px"><svg width="8" height="11" viewBox="0 0 8 11"><path d="M4 0a4 4 0 014 4c0 3-4 7-4 7S0 7 0 4a4 4 0 014-4z" fill="#eee"/><circle cx="4" cy="4" r="1.5" fill="#121314"/></svg><span>Pelkman Agency, 410 Birch Avenue, Suite C<br>Ashford Ridge, NJ 08712</span></div>

<div class="abs row" style="left:604px;top:1019px"><span>☎</span>(555) 482-7343</div>
<div class="abs row" style="left:604px;top:1042px"><span>▤</span>(555) 482-0170</div>
<div class="abs row" style="left:604px;top:1065px"><span>✉</span><u>admin@pelkmanagency.com</u></div>
<div class="abs row" style="left:604px;top:1087px"><svg width="8" height="11" viewBox="0 0 8 11"><path d="M4 0a4 4 0 014 4c0 3-4 7-4 7S0 7 0 4a4 4 0 014-4z" fill="#eee"/><circle cx="4" cy="4" r="1.5" fill="#121314"/></svg><span>Pelkman Agency, PO Box 274<br>62 Harbor Lane, Wexcombe, NJ 08091</span></div>

<div class="abs bottom"></div>
<div class="abs copy">© 2015 Pelkman Agency | All Rights Reserved.</div>
<span class="abs social" style="left:700px" aria-label="Social link"></span>
<span class="abs social" style="left:722px" aria-label="Social link"></span>
<span class="abs social" style="left:744px" aria-label="Feed link"></span>
<span class="abs social" style="left:766px" aria-label="Video link"></span>
</body>
</html>
```